Property Services Company Needs a Brochure Design

Looking for a new brochure design for an existing property services company.

We provide a range of property services from, market research, real estate brokerage, valuation and appraisal, property development and other real estate consulting services.

We would like a fresh modern brochure design with good graphics and features. Our colours are white, blue and orange.

The design should communicate, attention to detail, superior service delivery and distinction in results.
Updates

I would like the brochure to be roughly about 20 pages.

Containing the following,

1) An introduction
2) Contents Page
2) What we do
3) Our Services
4) Agency & Brokerage
5) Real Estate Consulting
6) Market Research
7) Appraisal & Valuation
8) Project Management
9) Property Development

I would also like icons to represent items 4,5,6,7,8 & 9, they should be represented vertically on each of the pages from the contents page and highlighted individually on the pages that they represent.. i.e. on appraisal & valuation page, all six icons will be arranged vertically and the appraisal and valuations icon will be highlighted.

I will also like to have images that depict the services on the various pages.

I have some pages I think will flow which I will upload shortly.

Industry/Entity Type

Real Estate

Font styles to use
Serif

Colors
f78f20
0455a3

```html
<!DOCTYPE html>
<html lang="en">
<head>
<meta charset="utf-8">
<title>Our Services – Brochure Spread</title>
<link rel="stylesheet" href="https://fonts.googleapis.com/css2?family=Tinos:wght@400;700&display=swap">
<style>
  :root {
    --backdrop: #e9e9e9;
    --paper: #ffffff;
    --brand-purple: #463d7c;
    --brand-orange: #e2773a;
    --photo-cream: #d9d2c4;
    --photo-warm: #b9a58a;
    --photo-glass: #cfd8dc;
    --photo-steel: #8e959b;
    --sketch-grey: #eef0f1;
  }
  * { box-sizing: border-box; margin: 0; padding: 0; }
  html, body {
    width: 1200px; height: 720px; overflow: hidden;
    background: var(--backdrop);
    font-family: "Tinos", "Times New Roman", serif;
  }
  .spread {
    position: absolute; left: 120px; top: 50px;
    width: 960px; height: 620px;
    display: flex;
    box-shadow: 0 10px 30px rgba(0,0,0,0.15);
  }
  .page {
    position: relative; width: 480px; height: 620px;
    background: var(--paper); overflow: hidden;
  }
  .page--left::after, .page--right::after {
    content: ""; position: absolute; top: 0; bottom: 0; width: 40px; pointer-events: none;
  }
  .page--left::after { right: 0; background: linear-gradient(to left, rgba(0,0,0,0.12), rgba(0,0,0,0)); }
  .page--right::after { left: 0; background: linear-gradient(to right, rgba(0,0,0,0.12), rgba(0,0,0,0)); }

  .rule { position: absolute; }
  .rule--purple { background: var(--brand-purple); height: 5px; }
  .rule--orange { background: var(--brand-orange); height: 7px; }

  .photo { position: absolute; }
  .photo--lobby {
    left: 0; top: 42px; width: 480px; height: 330px;
    background: linear-gradient(170deg, var(--photo-glass) 0%, var(--photo-cream) 45%, var(--photo-warm) 75%, var(--photo-cream) 100%);
  }
  .photo--office {
    left: 0; top: 42px; width: 310px; height: 240px;
    background: linear-gradient(160deg, #f3f4f5 0%, var(--photo-glass) 50%, var(--photo-steel) 100%);
  }
  .photo--sketch {
    left: 320px; top: 14px; width: 150px; height: 170px;
    background: linear-gradient(180deg, var(--sketch-grey), #ffffff);
  }

  .section-title {
    position: absolute; right: 24px; top: 412px;
    font-size: 26px; font-weight: 400; letter-spacing: 0.5px;
    color: var(--brand-purple);
  }

  .services-intro {
    position: absolute; left: 40px; top: 205px; width: 300px; height: 290px;
    background: var(--brand-orange); color: #fff;
    padding: 26px 22px 20px;
    font-size: 11px; line-height: 1.45;
  }
  .services-intro p + p { margin-top: 8px; }

  .page-number {
    position: absolute; width: 26px; height: 26px;
    background: var(--brand-purple); color: #fff;
    font-size: 12px; line-height: 26px; text-align: center;
  }
  .page--left .page-number { left: 40px; top: 536px; }
  .page--right .page-number { right: 40px; top: 536px; }

  .footer-band { position: absolute; left: 0; right: 0; top: 562px; }
  .footer-band .line { height: 4px; background: var(--brand-purple); }
  .footer-band .band { height: 16px; margin-top: 4px; background: var(--brand-orange); }
</style>
</head>
<body>
  <main class="spread">
    <section class="page page--left">
      <div class="rule rule--purple" style="left:70px; top:30px; width:120px;"></div>
      <div class="rule rule--orange" style="left:198px; top:29px; width:282px;"></div>
      <div class="photo photo--lobby" role="img" aria-label="Photo of a bright, modern office lobby with glass walls and polished floor"></div>
      <h1 class="section-title">OUR SERVICES</h1>
      <div class="page-number">5</div>
      <div class="footer-band"><div class="line"></div><div class="band"></div></div>
    </section>

    <section class="page page--right">
      <div class="rule rule--orange" style="left:0; top:29px; width:112px;"></div>
      <div class="rule rule--purple" style="left:120px; top:30px; width:112px;"></div>
      <div class="photo photo--office" role="img" aria-label="Photo of a modern office with a glass desk and executive chair"></div>
      <div class="photo photo--sketch" role="img" aria-label="Light line drawing of city buildings"></div>
      <div class="services-intro">
        <p>Our clients depend on our ability to draw on years of experience in the local market, our professionals know their communities and the property market needs and can, and provide knowledgeable, creative solutions to all their real estate needs.</p>
        <p>We currently provide services to corporations, financial institutions, government agencies, public sector entities, developers and investors. Our knowledge, expertise, experience and technological resources allow us to be a superior service provider. We currently provide services to corporations, financial institutions, government agencies, public sector entities, developers and investors. Our knowledge, expertise, experience and technological resources allow us to be a superior service provider.</p>
      </div>
      <div class="page-number">6</div>
      <div class="footer-band"><div class="line"></div><div class="band"></div></div>
    </section>
  </main>
</body>
</html>
```